Product Description page for Hullwrap.com, References here just need a clean up redesign

Hi, were working on updating the product description page of our site hullwrap.com

Attached is a reference of what we drew on paint. We want to keep it pretty much the same as far as whats on there, the components with a few small adjustments and a clean actually designed look.

1. We want to remove the tabs (product description, warranty, reviews) and put it all in that main content area stretching down into sections. IE: Product Description section, followed by reviews, followed by warranty, below each other.
2. The side bar needs to be redesigned as far as the look and feel but the content and whats in there should stay the same.
3. The main banner area will be replaced shortly you do not have to worry about that.
4. Include a section or box for people to put in their email for a free Ebook.

Target Market(s)

people looking to easily view our boat cover products and buy without having to click too often or leave the page.

Industry/Entity Type

Online Shopping

Number of Pages Required

1 page

Requirements
Must have
• - Must update the sidebar
• - Must update the content area to remove the tabs and put the content from each tab sectioned off below each other (dummy text is fine for now for the tabs you cant view)
Nice to have
• - Cool place thats clean and functional to insert a section for people to put in their email to receive a free ebook
Should not have
• - too much change, we already know what we want and have a solid reference to work from.

```html
<!DOCTYPE html>
<html lang="en">
<head>
<meta charset="utf-8">
<title>Boat Cover up to 19'5" Long and 90" Wide</title>
<link href="https://fonts.googleapis.com/css2?family=Open+Sans:wght@400;600;700&display=swap" rel="stylesheet">
<style>
:root{
  --navy:#1e2a47;
  --red:#c8242b;
  --blue:#2f6fb5;
  --ink:#3a3a3a;
  --muted:#8a8f98;
  --line:#dfe2e7;
  --panel:#f5f6f8;
  --white:#ffffff;
  --star:#e0a21b;
  --green:#2e8b3e;
}
*{box-sizing:border-box;margin:0;padding:0}
html,body{width:742px;height:1200px;overflow:hidden;background:var(--white)}
body{font-family:"Open Sans",Arial,sans-serif;color:var(--ink);font-size:5.6px;line-height:9px}
.page{position:relative;width:742px;height:1200px;overflow:hidden}
.title-bar{height:20px;background:var(--navy);color:var(--white);font-weight:700;font-size:12px;line-height:20px;text-align:center}
.breadcrumb{position:absolute;left:42px;top:23px;color:var(--muted);font-size:4.6px;line-height:6px}
.product-photo{position:absolute;left:42px;top:32px;width:463px;height:98px;background:linear-gradient(180deg,#eef0f3,#c9ced6 70%,#e8eaee)}
.content{position:absolute;left:42px;top:140px;width:463px}
.content h2{font-size:7px;line-height:10px;font-weight:700;color:var(--navy);margin:0 0 5px;padding-bottom:2px;border-bottom:1px solid var(--line)}
.content h3{font-size:5.8px;line-height:9px;font-weight:700;color:var(--navy);margin:16px 0 3px}
.content p{margin-bottom:7px}
.features{list-style:none;margin:3px 0 12px}
.features li{padding-left:7px;position:relative;line-height:9.5px}
.features li::before{content:"";position:absolute;left:0;top:3.6px;width:2.4px;height:2.4px;background:var(--navy);border-radius:50%}
.review{border-bottom:1px solid var(--line);padding:5px 0}
.review .who{font-weight:700;color:var(--navy)}
.stars{color:var(--star);letter-spacing:.5px}
.section{margin-top:14px}
.warranty p{margin-bottom:18px;line-height:10px}
.sidebar{position:absolute;left:520px;top:32px;width:180px}
.price-box{border:1px solid var(--line);padding:6px 7px}
.price{color:var(--red);font-size:11px;font-weight:700;line-height:14px}
.spec{display:flex;justify-content:space-between;border-bottom:1px dotted var(--line);padding:1px 0;font-size:4.8px;line-height:8px}
.spec b{color:var(--navy)}
.stock{color:var(--green);font-weight:600}
.qty{display:flex;gap:4px;align-items:center;margin-top:6px}
.qty span{width:18px;height:9px;border:1px solid var(--line);text-align:center;line-height:8px}
.cart-btn{display:block;margin:7px auto 2px;width:72px;height:14px;background:var(--blue);color:var(--white);font-weight:700;font-size:5.6px;line-height:14px;text-align:center;border-radius:2px}
.ebook{margin-top:8px;background:var(--panel);border:1px solid var(--line);padding:6px 7px;text-align:center}
.ebook h4{color:var(--blue);font-size:8px;line-height:10px}
.ebook .field{height:11px;border:1px solid var(--line);background:var(--white);margin:4px 0;text-align:left;padding-left:4px;color:var(--muted);line-height:10px}
.ebook .send{display:inline-block;width:48px;height:11px;background:var(--navy);color:var(--white);font-weight:700;line-height:11px;border-radius:2px}
.band{margin-top:8px;background:var(--navy);color:var(--white);font-weight:700;font-size:5.8px;line-height:9px;padding:3px 6px}
.item{display:flex;gap:5px;padding:4px 2px;border-bottom:1px solid var(--line)}
.thumb{width:26px;height:20px;background:linear-gradient(135deg,#cfd4dc,#9aa3b1);flex:none}
.item .name{color:var(--blue);font-weight:600}
.item .cost{color:var(--red);font-weight:700}
.search{display:flex;margin-top:4px}
.search .field{flex:1;height:12px;border:1px solid var(--line);border-right:0;padding-left:4px;line-height:11px;color:var(--muted)}
.search .go{width:14px;height:12px;background:var(--navy)}
</style>
</head>
<body>
<div class="page">
  <header class="title-bar">up to 19'5" Long and 90" Wide</header>
  <div class="breadcrumb">Home › Boat Covers › Custom Fit Boat Covers › up to 19'5" Long and 90" Wide</div>

  <div class="product-photo" role="img" aria-label="Grey fitted boat cover on a runabout boat sitting on a trailer"></div>

  <main class="content">
    <h2>Description</h2>
    <p>Built tough for everyday storage and towing, this cover fits V-hull and tri-hull runabouts with outboard or stern drive. Marine grade fabric resists fading, mildew and water while staying breathable, so your boat stays dry and clean season after season. Elastic hem and tie-down straps keep a snug fit on the road.</p>
    <ul class="features">
      <li>Fits 17'6" to 19'5" long boats with a beam up to 90"</li>
      <li>600 denier polyester with a water repellent finish</li>
      <li>Full elastic hem for a tight, wrinkle free fit</li>
      <li>Quick release tie-down straps included for trailering</li>
      <li>Air vents reduce wind lift and help prevent condensation</li>
      <li>Storage bag included, folds compact for easy carry</li>
      <li>Backed by a five year limited manufacturer warranty</li>
      <li>Free shipping on every cover ordered in the lower states</li>
    </ul>

    <section class="section">
      <h2>Reviews</h2>
      <div class="review"><span class="stars">★★★★★</span> <span class="who">Mark T.</span><br>Fit my bowrider perfectly. Straps were easy and the cover held up through a windy winter without a tear.</div>
      <div class="review"><span class="stars">★★★★★</span> <span class="who">Dana R.</span><br>Great quality for the price. Shipping was quick and the storage bag is a nice touch for the garage.</div>
      <div class="review"><span class="stars">★★★★☆</span> <span class="who">Steve L.</span><br>Solid cover, slightly loose at the stern but the straps took care of it. Would order again for my other boat.</div>
    </section>

    <section class="section warranty">
      <h2>Warranty</h2>
      <h3>Terms of Coverage</h3>
      <p>Every cover is guaranteed against defects in material and workmanship for the full warranty period from the date of purchase. Normal wear, misuse, improper installation and damage caused by storms or accidents are not included in this coverage.</p>
      <p>Should a seam fail or the fabric lose its water resistance under normal use, contact our support team with your order number and a photo of the problem. We will review the claim and repair or replace the cover at no cost.</p>
      <h3>How to Make a Claim</h3>
      <p>Send an email to our support desk with your name, order number and a short description. Our team answers most claims within two business days and will explain the next steps, including any return shipping details.</p>
      <p>Please keep your original receipt or order confirmation, as it is required to process any warranty request. Covers bought from outside dealers may carry different terms.</p>
      <h3>Returns and Exchanges</h3>
      <p>Unused covers in their original packaging may be returned within thirty days for a full refund or exchange. Simply request a return label and ship the item back; refunds are issued once the cover arrives at our warehouse.</p>
      <p>If you ordered the wrong size, we are happy to exchange it for the correct fit. Use our sizing guide to measure centerline length and beam width before ordering a replacement.</p>
      <h3>Care Instructions</h3>
      <p>Clean the cover with mild soap and cool water, then let it dry fully before folding. Avoid harsh chemicals, bleach and machine drying, which can weaken the fabric and shorten its life.</p>
      <p>When trailering at highway speeds, always secure every strap and check the fit at each stop. A support pole helps water run off and stops pooling on the top of the cover.</p>
      <h3>Measuring Your Boat</h3>
      <p>Measure the centerline length from the tip of the bow straight back to the stern, not counting the swim platform or motor. Then measure the widest point of the beam to choose the right size range.</p>
      <p>Boats with tall windshields, towers or bow rails may need a larger size. If you are between two sizes, our team can help you pick the fit that suits your boat best.</p>
      <h3>Fit Guarantee</h3>
      <p>If the cover does not fit your boat as listed, let us know within thirty days and we will send the correct size at no extra charge, along with a prepaid label for the first cover.</p>
      <p>Our guarantee applies to covers ordered using the listed length and beam range. Custom orders made to your exact measurements are covered by the same promise.</p>
      <h3>Shipping Information</h3>
      <p>Orders placed before noon ship the same business day. Most customers receive their cover within three to five days. Tracking details are sent by email once your package leaves our warehouse.</p>
      <p>We want every boat owner to be fully happy with their purchase. If you have any questions about fit, fabric or warranty, our friendly team is ready to help by phone or email.</p>
    </section>
  </main>

  <aside class="sidebar">
    <div class="price-box">
      <div class="price">$231.50</div>
      <div class="spec"><span>Length</span><b>17'6" – 19'5"</b></div>
      <div class="spec"><span>Beam</span><b>up to 90"</b></div>
      <div class="spec"><span>Fabric</span><b>600D Polyester</b></div>
      <div class="spec"><span>Colour</span><b>Grey</b></div>
      <div class="spec"><span>Warranty</span><b>5 Years</b></div>
      <div class="spec"><span>Availability</span><span class="stock">In Stock</span></div>
      <div class="qty">Qty <span>1</span></div>
      <span class="cart-btn">ADD TO CART</span>
    </div>

    <div class="ebook">
      <h4>Free ebook</h4>
      <div>Get our boat care guide free in your inbox</div>
      <div class="field">Your email address</div>
      <span class="send">Send</span>
    </div>

    <div class="band">Frequently Purchased Together</div>
    <div class="item"><div class="thumb" role="img" aria-label="Cover support pole"></div><div><div class="name">Cover Support Pole</div><div class="cost">$24.75</div></div></div>
    <div class="item"><div class="thumb" role="img" aria-label="Tie-down strap set"></div><div><div class="name">Tie-Down Strap Kit</div><div class="cost">$18.90</div></div></div>
    <div class="item"><div class="thumb" role="img" aria-label="Motor hood cover"></div><div><div class="name">Outboard Motor Hood</div><div class="cost">$42.50</div></div></div>
    <div class="item"><div class="thumb" role="img" aria-label="Fabric cleaner bottle"></div><div><div class="name">Fabric Care Spray</div><div class="cost">$12.95</div></div></div>

    <div class="band">Looking for something else?</div>
    <div class="search"><div class="field">Search covers…</div><div class="go"></div></div>
  </aside>
</div>
</body>
</html>
```